Talkbridge Allies co-marketing flier

We want a flier that our partners (IT consultants) can hand out to their clients and that we can send to local businesses on their behalf to demonstrate that they can help customers purchase a phone system that has professional features that they would expect in a phone solution that costs thousands of dollars.

We want the brochure to look very professional with excellent layout and use of space.

The Talkbridge Allies corporate colour is green and more details can be found at www.talkbridgeallies.com.au.

We have attached a draft Word document that contains most of the information we need but please present the information in the way YOU believe it should be laid out.

We are looking for a designer who understands the concept and uses their own skills to produce a work of art.

Target Market(s)

small businesses that want to save money but also want a modern phone with lots of features

Industry/Entity Type

Marketing

Requirements
Must have
• Must have an image of the main phone and a cordless handset to indicate that they don't need wires to set the system up.

Must have our logo and website address

Must have a box or some "placeholder" where our partners can stamp or insert their details.

Must have a "call to action" saying "Contact us for a quote"

```html
<!DOCTYPE html>
<html lang="en">
<head>
<meta charset="utf-8">
<title>Talkbridge Allies – Phone System Flier</title>
<link rel="stylesheet" href="https://fonts.googleapis.com/css2?family=Courier+Prime:wght@400;700&family=Architects+Daughter&family=Open+Sans:wght@400;600&display=swap">
<style>
  :root {
    --maroon: #6e1f1f;
    --maroon-edge: #8c2c2c;
    --board-light: #6cc85a;
    --board-dark: #2b9440;
    --frame: #eeeeee;
    --note: #fbec7e;
    --note-shadow: rgba(0,0,0,0.28);
    --ink: #1c1c1c;
    --brand-green: #3aa64a;
    --white: #ffffff;
    --pin: #d8141a;
  }
  * { box-sizing: border-box; margin: 0; padding: 0; }
  html, body { width: 848px; height: 1200px; overflow: hidden; background: var(--white); }
  .flier { position: relative; width: 848px; height: 1200px; overflow: hidden; background: var(--frame); }
  .flier-edge { position: absolute; inset: 0; border: 8px solid var(--maroon); pointer-events: none; z-index: 10; }
  .board {
    position: absolute; left: 29px; top: 29px; width: 792px; height: 752px;
    background: radial-gradient(ellipse at 50% 30%, var(--board-light) 0%, var(--board-dark) 85%);
  }
  .shelf { position: absolute; left: 0; top: 0; }
  .title-plate {
    position: absolute; left: 75px; top: 17px; width: 700px; height: 60px;
    background: linear-gradient(180deg, #f2f2f2 0%, #c9c9c9 45%, #e4e4e4 55%, #b5b5b5 100%);
    box-shadow: 0 3px 6px rgba(0,0,0,0.35);
    display: flex; align-items: center; justify-content: center;
  }
  .title-plate h1 {
    font-family: "Courier Prime", "Courier New", monospace; font-weight: 400;
    font-size: 33px; color: #2a2a2a; text-shadow: 0 1px 0 rgba(255,255,255,0.6);
  }
  .screw {
    position: absolute; top: 24px; width: 11px; height: 11px; border-radius: 50%;
    background: radial-gradient(circle at 35% 35%, #eee, #777);
  }
  .screw.left { left: 14px; } .screw.right { right: 14px; }
  .intro, .tagline {
    position: absolute; left: 0; width: 848px; text-align: center;
    font-family: "Courier Prime", "Courier New", monospace; color: var(--ink);
  }
  .intro { top: 117px; font-size: 23px; line-height: 30px; }
  .tagline { top: 197px; font-size: 31px; }
  .note {
    position: absolute; left: 200px; top: 267px; width: 431px; height: 290px;
    background: var(--note); transform: rotate(-0.4deg);
    box-shadow: 2px 6px 10px var(--note-shadow);
    font-family: "Architects Daughter", cursive; color: var(--ink);
    padding: 39px 0 0 20px;
  }
  .note h2 { font-size: 15px; font-weight: 400; margin-bottom: 11px; }
  .features { list-style: none; }
  .features li { position: relative; font-size: 11px; height: 25px; padding-left: 61px; }
  .features li::before { content: "•"; position: absolute; left: 0; }
  .pin { position: absolute; left: 422px; top: 244px; }
  .desk-phone, .cordless {
    position: absolute;
    background: linear-gradient(165deg, #a6a6a6 0%, #4a4a4a 55%, #222 100%);
  }
  .desk-phone { left: 52px; top: 640px; width: 512px; height: 262px; border-radius: 26px 26px 30px 40px; }
  .cordless { left: 568px; top: 576px; width: 138px; height: 282px; border-radius: 34px 34px 12px 12px; }
  .brand { position: absolute; left: 46px; top: 1058px; display: flex; align-items: center; gap: 10px; }
  .brand .dot { width: 14px; height: 14px; border-radius: 50%; background: var(--brand-green); }
  .brand .name {
    font-family: "Courier Prime", "Courier New", monospace; font-weight: 700;
    font-size: 32px; color: var(--brand-green);
  }
  .company-details {
    position: absolute; left: 56px; top: 1116px;
    font-family: "Open Sans", Arial, sans-serif; font-size: 13.5px; line-height: 18px; color: var(--white);
  }
  .call-to-action {
    position: absolute; left: 504px; top: 1046px; width: 323px; text-align: center;
    font-family: "Courier Prime", "Courier New", monospace; font-weight: 700;
    font-size: 21px; color: var(--white);
  }
  .partner-stamp {
    position: absolute; left: 504px; top: 1081px; width: 323px; height: 92px;
    background: var(--white); border: 1px solid #9a9a9a;
  }
</style>
</head>
<body>
<div class="flier">
  <div class="board"></div>

  <svg class="shelf" width="848" height="1200" viewBox="0 0 848 1200" aria-hidden="true">
    <defs>
      <linearGradient id="maroonFade" x1="0" y1="0" x2="0" y2="1">
        <stop offset="0" stop-color="#7a2424"/>
        <stop offset="1" stop-color="#3e1010"/>
      </linearGradient>
    </defs>
    <rect x="0" y="781" width="848" height="419" fill="url(#maroonFade)"/>
    <polygon points="0,800 848,800 848,832 496,972 0,832" fill="#8c2c2c"/>
    <polygon points="0,800 848,800 848,814 496,955 0,814" fill="#ffffff"/>
  </svg>

  <div class="title-plate">
    <span class="screw left"></span>
    <h1>Looking for a new phone system?</h1>
    <span class="screw right"></span>
  </div>
  <p class="intro">Our proven VoIP solution comes with all<br>the professional features</p>
  <p class="tagline">It’s cheaper than you think.</p>

  <div class="note">
    <h2>Features include, but not limited, to:</h2>
    <ul class="features">
      <li>Very low line rental rates*</li>
      <li>10c local and national calls untimed</li>
      <li>Voicemail-to-email</li>
      <li>Bluetooth-to-mobile</li>
      <li>Direct in-dial to every extension</li>
      <li>Number portability (keep your number when you move)</li>
      <li>Call records via spreadsheet</li>
      <li>Flat rate local and national calls</li>
    </ul>
  </div>

  <svg class="pin" width="40" height="44" viewBox="0 0 40 44" aria-hidden="true">
    <line x1="12" y1="30" x2="4" y2="42" stroke="#555" stroke-width="2"/>
    <ellipse cx="22" cy="18" rx="14" ry="12" fill="var(--pin)"/>
    <ellipse cx="18" cy="14" rx="5" ry="3" fill="#ff7a7a"/>
  </svg>

  <div class="desk-phone" role="img" aria-label="Photo of a desk phone with corded handset and colour display"></div>
  <div class="cordless" role="img" aria-label="Photo of a cordless handset standing in its charging cradle"></div>

  <div class="brand">
    <span class="dot"></span>
    <span class="name">Talkbridge Allies</span>
  </div>
  <p class="company-details">corvane (456 Holdings Pty Ltd)<br>ABN: 12 345 678 901<br>www.talkbridgeallies.com.au</p>

  <p class="call-to-action">Contact us for a quote</p>
  <div class="partner-stamp" aria-label="Space for partner details"></div>

  <div class="flier-edge"></div>
</div>
</body>
</html>
```